Flyer Design Print Ad for Clothing Store

We are a modest women's clothing store. We are looking for a print ad 90*134 mm that is attention grabbing and can serve as a template for us going forward. We cannot use pictures of actual women. We need it to include our logo, store hours, physical address, website, phone number. We would use this template and change the call to action as necessary e. g. BOGO Sale, 30% off, flash sale, summer sale etc. Our colors are black and white and our fonts are Bodoni sans and Athens.

Target Market(s)

Women from teen to age 70

Industry/Entity Type

Women's clothing

Font styles to use
Other font styles liked:
• Athens, Bodoni Sans

Requirements
Must have
• Our, logo, phone number, website, address and store hours
Nice to have
• I'd like something that's not just our flat logo but something that will make someone pause to look
Should not have
• Pictures of women

```html
<!DOCTYPE html>
<html lang="en">
<head>
<meta charset="utf-8">
<title>Lindenway – BOGO Sale Flyer</title>
<link rel="stylesheet" href="https://fonts.googleapis.com/css2?family=Marcellus&family=Bungee+Inline&display=swap">
<style>
  :root {
    --ink: #121822;
    --paper: #ffffff;
    --backdrop: #ffffff;
    --rule-grey: #6d7178;
    --floral-mid: #9a9a9a;
    --floral-light: #d4d4d4;
    --display: "Marcellus", serif;
    --deco: "Bungee Inline", sans-serif;
  }
  html, body {
    margin: 0;
    padding: 0;
    width: 900px;
    height: 1200px;
    overflow: hidden;
    background: var(--backdrop);
  }
  .flyer {
    position: absolute;
    left: 138px;
    top: 131px;
    width: 624px;
    height: 932px;
    background: var(--paper);
    box-shadow: 2px 4px 10px rgba(0,0,0,0.35);
    overflow: hidden;
  }
  .floral { position: absolute; display: block; }
  .floral--top { left: 0; top: 0; width: 480px; height: 460px; }
  .floral--bottom { right: 0; top: 475px; width: 380px; height: 457px; }

  .sale-disc {
    position: absolute;
    left: 32px;
    top: 182px;
    width: 560px;
    height: 560px;
    border-radius: 50%;
    background: var(--ink);
    color: var(--paper);
  }
  .brand-mark {
    position: absolute;
    left: 232px;
    top: 48px;
    width: 92px;
    height: 92px;
    border: 2px solid var(--paper);
    border-radius: 50%;
    box-sizing: border-box;
  }
  .brand {
    position: absolute;
    top: 152px;
    width: 100%;
    text-align: center;
    font-family: var(--display);
    font-size: 25px;
    letter-spacing: 6px;
  }
  .headline {
    position: absolute;
    left: 72px;
    top: 197px;
    margin: 0;
    font-family: var(--display);
    font-weight: 400;
    font-size: 76px;
    line-height: 1;
    letter-spacing: 1px;
  }
  .offer {
    position: absolute;
    right: 84px;
    top: 280px;
    font-family: var(--display);
    font-size: 50px;
    line-height: 1;
  }
  .offer-rules {
    position: absolute;
    left: 76px;
    top: 294px;
    width: 171px;
    height: 20px;
  }
  .venue {
    position: absolute;
    top: 352px;
    width: 100%;
    text-align: center;
    font-family: var(--deco);
    font-size: 25px;
    line-height: 1.1;
  }
  .venue-note {
    position: absolute;
    top: 392px;
    width: 100%;
    text-align: center;
    font-family: var(--deco);
    font-size: 20px;
    line-height: 1.1;
  }
  .venue-alt {
    position: absolute;
    left: 95px;
    top: 438px;
    width: 351px;
    height: 29px;
    border-top: 1px solid var(--paper);
    border-bottom: 1px solid var(--paper);
    display: flex;
    align-items: center;
    justify-content: center;
    font-family: var(--deco);
    font-size: 12px;
  }
  .venue-alt .num { font-family: var(--display); font-size: 16px; margin: 0 4px; }

  .info-box {
    position: absolute;
    left: 62px;
    top: 787px;
    width: 497px;
    height: 112px;
    border: 1.5px solid var(--ink);
    background: rgba(255,255,255,0.8);
    box-sizing: border-box;
    display: flex;
    flex-direction: column;
    justify-content: center;
    align-items: center;
    gap: 4px;
    font-family: var(--display);
    font-size: 22px;
    line-height: 1.15;
    color: var(--ink);
    white-space: nowrap;
  }
  .info-box .hours span + span { margin-left: 22px; }
  .info-box .contact { font-size: 15px; letter-spacing: 0.5px; }
  .info-box .contact span + span { margin-left: 18px; }
  .info-box .pip {
    position: absolute;
    left: 50%;
    width: 20px;
    height: 12px;
    margin-left: -10px;
  }
  .info-box .pip--top { top: -7px; }
  .info-box .pip--bottom { bottom: -7px; }
</style>
</head>
<body>
  <main class="flyer">
    <svg class="floral floral--top" viewBox="0 0 480 460" role="img" aria-label="Grey botanical illustration of flowers, leaves and berry sprigs in the top-left corner">
      <defs>
        <radialGradient id="floralTopTone" cx="0.2" cy="0.2" r="0.9">
          <stop offset="0" stop-color="var(--floral-mid)"/>
          <stop offset="0.6" stop-color="var(--floral-light)"/>
          <stop offset="1" stop-color="var(--floral-light)" stop-opacity="0"/>
        </radialGradient>
      </defs>
      <path d="M0 0 H480 C420 80 380 160 300 200 C220 240 160 300 90 430 L0 460 Z" fill="url(#floralTopTone)"/>
    </svg>
    <svg class="floral floral--bottom" viewBox="0 0 380 457" role="img" aria-label="Grey botanical illustration of flowers, leaves and berry sprigs in the bottom-right corner">
      <defs>
        <radialGradient id="floralBottomTone" cx="0.85" cy="0.6" r="0.9">
          <stop offset="0" stop-color="var(--floral-mid)"/>
          <stop offset="0.6" stop-color="var(--floral-light)"/>
          <stop offset="1" stop-color="var(--floral-light)" stop-opacity="0"/>
        </radialGradient>
      </defs>
      <path d="M380 0 V457 H0 C40 400 80 360 150 320 C230 270 300 180 330 80 Z" fill="url(#floralBottomTone)"/>
    </svg>

    <section class="sale-disc">
      <div class="brand-mark" aria-hidden="true"></div>
      <div class="brand">LINDENWAY</div>
      <h1 class="headline">BOGO SALE</h1>
      <svg class="offer-rules" viewBox="0 0 171 20" aria-hidden="true">
        <line x1="0" y1="2" x2="171" y2="2" stroke="var(--rule-grey)" stroke-width="2"/>
        <line x1="0" y1="10" x2="171" y2="10" stroke="var(--rule-grey)" stroke-width="2"/>
        <line x1="0" y1="18" x2="171" y2="18" stroke="var(--rule-grey)" stroke-width="2"/>
      </svg>
      <div class="offer">30% OFF</div>
      <div class="venue">CEDAR HILL SHOPPING CENTER</div>
      <div class="venue-note">(NEXT TO THE MAIN PLAZA)</div>
      <div class="venue-alt">IT CAN ALSO BE REACHED FROM <span class="num">16</span> CEDAR HILL BLVD</div>
    </section>

    <section class="info-box">
      <svg class="pip pip--top" viewBox="0 0 20 12" aria-hidden="true"><path d="M0 6 Q10 -4 20 6 Q10 16 0 6Z" fill="var(--ink)"/></svg>
      <div class="buses">BUSES 21, 22, 39, 41, 45, 52, 59, 65, 68, 69, 77</div>
      <div class="hours"><span>S-TH- 10:30-12:30</span><span>SUN-TH- 20:30 - 22:30</span></div>
      <div class="contact"><span>(555) 014-2273</span><span>www.lindenway.example</span></div>
      <svg class="pip pip--bottom" viewBox="0 0 20 12" aria-hidden="true"><path d="M0 6 Q10 -4 20 6 Q10 16 0 6Z" fill="var(--ink)"/></svg>
    </section>
  </main>
</body>
</html>
```